DL SIZED ONE SIDED BROCHURE FOR CLEANING AND GARDENING SERVICE

business name: Q&T property services
services provided: Strata cleaning,lawn mowing,hedge trimming,garden maintainance,lawn repair,weed spraying/removal, rubbish removal.
10 years experience and fully insured.
obligation free quotes.
phone number:contact vince 0427093516
email: qtpropertyservices@mailbox-example.net
slogan: when quality matters ring Q&T
Q&T logo would be nice but not essential
DL size in inches: 3.9in × 8.2in
DL size in millimetres: 100mm × 210mm
DL size in centimetres: 10cm x 21cm
Updates
doing good guys no suggestions except being original
Target Market(s)
real estate agents, private home owners, contractors.
Industry/Entity Type
Business
Look and feel
Each slider illustrates characteristics of the customer's brand and the style your logo design should communicate.

```html
<!DOCTYPE html>
<html lang="en">
<head>
<meta charset="utf-8">
<title>Q&amp;T Property Services – DL Brochure</title>
<link rel="stylesheet" href="https://fonts.googleapis.com/css2?family=Arimo:ital,wght@0,700;1,700&family=PT+Serif:wght@700&display=swap">
<style>
  :root {
    --green-deep: #16691f;
    --green-mid: #2b9a35;
    --green-light: #6cc04a;
    --lime: #d9e82c;
    --yellow: #ffd800;
    --slogan-yellow: #f5e11a;
    --red: #d6221b;
    --red-dark: #a5140f;
    --white: #ffffff;
  }
  html, body { margin: 0; padding: 0; overflow: hidden; background: #e9ece6; }
  .brochure {
    position: relative; width: 1200px; height: 576px; overflow: hidden;
    background: var(--green-deep);
    font-family: "Arimo", Arial, sans-serif;
  }
  .backdrop { position: absolute; inset: 0; }
  .brand { position: absolute; left: 46px; top: 28px; color: var(--white); }
  .brand-row { display: flex; align-items: center; gap: 14px; }
  .brand-mark { width: 26px; height: 26px; border-radius: 50%; background: var(--white); }
  .brand-name {
    font-family: "PT Serif", Georgia, serif; font-weight: 700;
    font-size: 78px; line-height: 1; letter-spacing: -1px;
  }
  .brand-services {
    font-family: "PT Serif", Georgia, serif; font-weight: 700;
    font-size: 34px; line-height: 1.02;
  }
  .slogan {
    margin-top: 6px; font-style: italic; font-weight: 700; font-size: 21px;
    color: var(--slogan-yellow);
  }
  .experience {
    position: absolute; left: 454px; top: 10px; width: 332px; height: 138px;
    background: var(--lime); border-radius: 0 0 40px 0;
    display: flex; align-items: center; padding-left: 14px; box-sizing: border-box;
  }
  .experience-number { color: var(--red); font-size: 118px; font-weight: 700; line-height: 1; letter-spacing: -4px; }
  .experience-text { color: var(--green-deep); font-size: 31px; font-weight: 700; line-height: 1.02; margin-left: 10px; }
  .experience-text .small { font-size: 22px; font-style: italic; }
  .contact-banner {
    position: absolute; right: 40px; top: 40px; transform: rotate(21deg);
    color: var(--red); font-weight: 700; text-align: center; line-height: 1.05;
  }
  .contact-name { font-size: 34px; }
  .contact-phone { font-size: 40px; }
  .services {
    position: absolute; left: 66px; top: 200px; margin: 0; padding: 0; list-style: none;
    color: var(--white); font-weight: 700; font-size: 31px;
  }
  .services li { position: relative; padding-left: 52px; height: 44px; line-height: 44px; }
  .services li::before {
    content: ""; position: absolute; left: 0; top: 14px; width: 16px; height: 16px;
    border-radius: 50%; background: var(--white);
  }
  .email {
    position: absolute; left: 50px; bottom: 28px; color: var(--slogan-yellow);
    font-size: 20px; font-weight: 700;
  }
  .quote-button {
    position: absolute; right: 0; bottom: 22px; width: 284px; height: 56px;
    background: linear-gradient(var(--red), var(--red-dark));
    border-radius: 18px 0 0 18px; color: var(--yellow);
    font-size: 22px; font-weight: 700; display: flex; align-items: center; justify-content: center;
  }
</style>
</head>
<body>
<div class="brochure">
  <svg class="backdrop" width="1200" height="576" viewBox="0 0 1200 576">
    <defs>
      <linearGradient id="panel" x1="0" y1="0" x2="0" y2="1">
        <stop offset="0" stop-color="#1f8a2a"/>
        <stop offset="1" stop-color="#14601c"/>
      </linearGradient>
      <linearGradient id="garden" x1="0" y1="0" x2="1" y2="1">
        <stop offset="0" stop-color="#4f8e3a"/>
        <stop offset="0.45" stop-color="#c65fa6"/>
        <stop offset="0.7" stop-color="#7aa94a"/>
        <stop offset="1" stop-color="#9a9c8e"/>
      </linearGradient>
      <linearGradient id="lawn" x1="0" y1="0" x2="0" y2="1">
        <stop offset="0" stop-color="#8fb3d6"/>
        <stop offset="0.4" stop-color="#d2584a"/>
        <stop offset="1" stop-color="#4c9a35"/>
      </linearGradient>
    </defs>
    <rect width="1200" height="576" fill="url(#panel)"/>
    <g role="img" aria-label="Photo of a flowering garden with pink rhododendrons, trees and a paved path">
      <path d="M600 120 C 530 260 520 420 560 576 L1200 576 L1200 110 Z" fill="url(#garden)"/>
    </g>
    <path d="M0 0 L1200 0 L1200 60 C 900 160 700 60 540 150 C 420 210 300 180 0 170 Z" fill="var(--green-mid)"/>
    <path d="M0 0 L1200 0 L1200 30 C 900 120 700 30 540 120 C 420 180 300 150 0 150 Z" fill="var(--green-deep)"/>
    <path d="M1200 60 C 900 160 700 60 540 150 C 620 120 800 190 1200 120 Z" fill="var(--green-light)"/>
    <polygon points="930,0 1200,0 1200,270" fill="var(--yellow)"/>
    <g role="img" aria-label="Round photo of a formal flower garden with red flower beds and lawn">
      <circle cx="462" cy="384" r="86" fill="var(--white)"/>
      <circle cx="462" cy="384" r="80" fill="url(#lawn)"/>
    </g>
  </svg>

  <div class="brand">
    <div class="brand-row">
      <span class="brand-name">Q&amp;T</span>
      <span class="brand-services">Property<br>Services</span>
      <span class="brand-mark"></span>
    </div>
    <div class="slogan">When quality matters ring Q&amp;T</div>
  </div>

  <div class="experience">
    <span class="experience-number">10</span>
    <span class="experience-text"><span class="small">years</span><br>experience<br>fully insured</span>
  </div>

  <div class="contact-banner">
    <div class="contact-name">Vince</div>
    <div class="contact-phone">0427093516</div>
  </div>

  <ul class="services">
    <li>Weed Spraying/Removal,</li>
    <li>Garden Maintainance,</li>
    <li>Rubbish Removal</li>
    <li>Hedge Trimming,</li>
    <li>Strata Cleaning,</li>
    <li>Lawn Mowing,</li>
    <li>Lawn Repair,</li>
  </ul>

  <div class="email">email: qtpropertyservices@mailbox-example.net</div>

  <div class="quote-button">Obligation Free Quotes</div>
</div>
</body>
</html>
```